Webdesign plus CSS for a German company data register

We need a unique and attractive webdesign including CSS development for a website (https://kontorfeld.de/) of our newly founded company. We collect company data from several public registers to display them aggregated.

Your design should communicate science, data security, a business note and perhaps a slice of nerdness. Elements - like color and layout - of our logo should also be found in your design.

Target Market(s)

banks, insurance companies, authorities etc.

Industry/Entity Type

Internet

Coding

Coded - Design and coding required

Number of Pages Required

3 page

Font styles to use
Sans Serif

Requirements
Must have
• mockups, CSS

eye catching, easy to read / navigate
Nice to have
• pictogramms / logos for essential content

```html
<!DOCTYPE html>
<html lang="en">
<head>
<meta charset="utf-8">
<title>Kontorfeld – Commercial register data</title>
<link href="https://fonts.googleapis.com/css2?family=Titillium+Web:wght@400;600;700;900&family=Open+Sans:wght@400;600&display=swap" rel="stylesheet">
<style>
:root{
  --orange:#e8461e;
  --orange-dark:#c9350f;
  --ink:#1b1b1b;
  --grey:#5b5b5b;
  --light:#f3f3f3;
  --line:#e2e2e2;
  --white:#ffffff;
  --footer:#151515;
}
*{box-sizing:border-box;margin:0;padding:0}
html,body{width:1200px;height:3496px;overflow:hidden}
body{font-family:"Open Sans",Arial,sans-serif;color:var(--ink);background:var(--white);position:relative}
.head-font{font-family:"Titillium Web",Arial,sans-serif}

/* Header */
.site-header{position:absolute;top:0;left:0;width:1200px;height:90px;background:var(--white);display:flex;align-items:center;padding:0 48px;z-index:5}
.brand{display:flex;align-items:center;gap:10px;font-family:"Titillium Web",sans-serif;font-weight:700;font-size:26px;color:var(--orange);letter-spacing:1px}
.brand-square{width:22px;height:22px;background:var(--orange)}
.main-nav{display:flex;gap:26px;margin-left:80px;font-family:"Titillium Web",sans-serif;font-weight:700;font-size:16px}
.main-nav a{color:var(--ink);text-decoration:none}
.main-nav a.active{color:var(--orange);border-bottom:2px solid var(--orange)}
.head-actions{margin-left:auto;display:flex;gap:10px}
.btn{font-family:"Titillium Web",sans-serif;font-weight:700;font-size:14px;color:var(--white);padding:9px 20px;text-decoration:none;letter-spacing:.5px}
.btn-orange{background:var(--orange)}
.btn-dark{background:#6a6a6a}

/* Hero */
.hero{position:absolute;top:90px;left:0;width:1200px;height:790px}
.hero-photo{position:absolute;inset:0;background:linear-gradient(120deg,#2e3236 0%,#4a4f55 35%,#23272b 70%,#3a3e43 100%)}
.hero-shade{position:absolute;inset:0;background:rgba(0,0,0,.35)}
.hero-title{position:absolute;top:275px;width:100%;text-align:center;color:var(--white);font-family:"Titillium Web",sans-serif;font-weight:700;font-size:64px;letter-spacing:2px}
.hero-sub{position:absolute;top:372px;width:100%;text-align:center;color:var(--white);font-family:"Titillium Web",sans-serif;font-weight:600;font-size:19px;letter-spacing:1px}
.hero-switch{position:absolute;top:430px;left:310px;width:580px;height:110px;display:flex;align-items:center;justify-content:center;gap:40px}
.switch-item{display:flex;align-items:center;gap:12px;color:var(--white);font-family:"Titillium Web",sans-serif;font-weight:700;font-size:26px}
.switch-item .label{border-bottom:3px solid var(--orange);padding-bottom:2px}
.switch-core{width:96px;height:96px;border-radius:50%;background:var(--orange);border:5px solid rgba(255,255,255,.8)}
.hero-edge{position:absolute;left:0;bottom:0;width:1200px;height:200px}

/* About */
.about{position:absolute;top:900px;left:0;width:1200px;height:420px}
.about-visual{position:absolute;left:150px;top:20px;width:440px;height:300px;background:linear-gradient(135deg,#e8461e 0%,#f2a07f 50%,#8c8c8c 100%);clip-path:polygon(0 0,100% 0,100% 100%,0 100%)}
.about-text{position:absolute;left:690px;top:30px;width:380px}
.section-title{font-family:"Titillium Web",sans-serif;font-weight:700;font-size:40px;color:var(--ink);letter-spacing:1px}
.section-title .accent{color:var(--orange)}
.about-list{list-style:none;margin-top:14px}
.about-list li{position:relative;padding-left:24px;font-size:14px;line-height:1.55;color:var(--grey);margin-bottom:12px}
.about-list li::before{content:"";position:absolute;left:0;top:6px;width:11px;height:11px;background:var(--orange)}
.about-text .btn{display:inline-block;margin-top:8px;font-size:13px;padding:8px 16px}

/* Stats */
.stats{position:absolute;top:1340px;left:0;width:1200px;height:330px}
.stats .section-title{text-align:center;margin-top:20px}
.stat-row{position:absolute;top:100px;left:0;width:1200px;display:flex;justify-content:center;gap:40px}
.stat{width:190px;height:190px;border-radius:50%;border:7px solid #6b6b6b;border-top-color:var(--orange);border-right-color:var(--orange);background:var(--white);display:flex;flex-direction:column;align-items:center;justify-content:center}
.stat-value{font-family:"Titillium Web",sans-serif;font-weight:700;font-size:52px;line-height:1}
.stat-label{font-size:12px;color:var(--grey);margin-top:6px}

/* Companies table */
.companies{position:absolute;top:1780px;left:0;width:1200px;height:640px}
.companies .section-title{text-align:center;margin-top:20px}
.company-table{position:absolute;top:150px;left:140px;width:920px;border-collapse:collapse;font-size:13px;box-shadow:0 4px 14px rgba(0,0,0,.08)}
.company-table th{background:var(--orange);color:var(--white);font-family:"Titillium Web",sans-serif;font-weight:700;text-align:left;padding:12px 14px;font-size:14px}
.company-table td{padding:12px 14px;border-bottom:1px solid var(--line);color:var(--grey)}
.company-table tr:nth-child(even) td{background:#fafafa}

/* Call to action */
.cta{position:absolute;top:2480px;left:0;width:1200px;height:620px}
.cta-photo{position:absolute;inset:0;background:linear-gradient(135deg,#f07a3e 0%,#e8461e 45%,#b8330f 100%);clip-path:polygon(0 18%,100% 0,100% 100%,0 100%)}
.cta-title{position:absolute;top:260px;width:100%;text-align:center;color:var(--white);font-family:"Titillium Web",sans-serif;font-weight:700;font-size:46px;line-height:1.15;letter-spacing:1px}
.cta .btn{position:absolute;top:398px;left:536px;background:#6a6a6a;font-size:15px;padding:11px 22px}

/* Footer */
.site-footer{position:absolute;top:3060px;left:0;width:1200px;height:436px;background:var(--footer)}
.footer-edge{position:absolute;top:-60px;left:0;width:1200px;height:62px}
.footer-brand{position:absolute;left:90px;top:90px}
.footer-brand .brand{font-size:30px}
.footer-tagline{color:#bdbdbd;font-size:11px;letter-spacing:2px;margin-top:6px}
.social{position:absolute;left:432px;top:110px;display:flex;gap:14px}
.social span{width:30px;height:30px;border-radius:50%;border:2px solid #cfcfcf}
.quick-links{position:absolute;right:90px;top:80px;text-align:right}
.quick-links h3{color:var(--white);font-family:"Titillium Web",sans-serif;font-size:20px;font-weight:700;letter-spacing:1px}
.quick-links nav{margin-top:36px;display:flex;gap:18px}
.quick-links a{color:var(--white);font-size:14px;text-decoration:none}
.copyright{position:absolute;left:0;top:310px;width:100%;border-top:1px solid #333;padding-top:24px;text-align:center;color:#bdbdbd;font-size:13px}
</style>
</head>
<body>

<header class="site-header">
  <div class="brand"><span class="brand-square"></span>KONTORFELD</div>
  <nav class="main-nav">
    <a class="active" href="https://kontorfeld.de/">HOME</a>
    <a href="#about">ABOUT</a>
    <a href="#">SERVICES</a>
    <a href="#">SUPPORT</a>
    <a href="#">CONTACT</a>
  </nav>
  <div class="head-actions">
    <a class="btn btn-orange" href="#">REGISTRATION</a>
    <a class="btn btn-dark" href="#">LOGIN</a>
  </div>
</header>

<section class="hero">
  <div class="hero-photo" role="img" aria-label="Two business people walking through a server room"></div>
  <div class="hero-shade"></div>
  <h1 class="hero-title">KONTORFELD</h1>
  <p class="hero-sub">COMMERCIAL REGISTER DATA, COMPANY DATA AND PERSONAL DATA</p>
  <div class="hero-switch">
    <div class="switch-item">
      <svg width="44" height="44" viewBox="0 0 44 44" fill="none" stroke="#fff" stroke-width="2"><rect x="6" y="12" width="14" height="26"/><rect x="22" y="4" width="16" height="34"/><path d="M10 18h6M10 24h6M10 30h6M26 10h8M26 16h8M26 22h8M26 28h8"/></svg>
      <span class="label">COMPANIES</span>
    </div>
    <div class="switch-core"></div>
    <div class="switch-item">
      <svg width="44" height="44" viewBox="0 0 44 44" fill="none" stroke="#fff" stroke-width="2"><circle cx="22" cy="14" r="8"/><path d="M6 40c0-10 7-16 16-16s16 6 16 16"/></svg>
      <span class="label">PERSONS</span>
    </div>
  </div>
  <svg class="hero-edge" viewBox="0 0 1200 200" preserveAspectRatio="none">
    <polygon points="0,200 1200,40 1200,200" fill="#ffffff"/>
    <polygon points="760,200 1200,60 1200,110 940,200" fill="#e8461e"/>
    <polygon points="0,200 0,170 600,200" fill="#ffffff"/>
  </svg>
</section>

<section class="about" id="about">
  <div class="about-visual" role="img" aria-label="Photo of a handshake between business partners"></div>
  <div class="about-text">
    <h2 class="section-title">ABOUT <span class="accent">US</span></h2>
    <ul class="about-list">
      <li>We have made it our goal to become a reputable provider of correct commercial register data, company data and personal data.</li>
      <li>Our efforts are honest and uncomplicated data about people, companies, communities and associations.</li>
      <li>Our goal is an absolutely transparent, honest and fair publication.</li>
    </ul>
    <a class="btn btn-orange" href="#">READ MORE &#9654;</a>
  </div>
</section>

<section class="stats">
  <h2 class="section-title">OUR STATS</h2>
  <div class="stat-row">
    <div class="stat"><span class="stat-value head-font">75%</span><span class="stat-label">Registers covered</span></div>
    <div class="stat"><span class="stat-value head-font">9,358</span><span class="stat-label">Companies indexed</span></div>
    <div class="stat"><span class="stat-value head-font">12</span><span class="stat-label">Data sources</span></div>
    <div class="stat"><span class="stat-value head-font">35.85</span><span class="stat-label">Updates per minute</span></div>
  </div>
</section>

<section class="companies">
  <h2 class="section-title">COMPANIES OF INTEREST</h2>
  <table class="company-table">
    <thead><tr><th>DESIGNATION</th><th>TYPE</th><th>BUNDESLAND</th><th>NUMBER</th><th>UPDATED</th></tr></thead>
    <tbody>
      <tr><td>Nordlicht Optik GmbH &amp; Co. KG</td><td>Name entry</td><td>Bavaria</td><td>23</td><td>12.02.19 AM</td></tr>
      <tr><td>Nordlicht Optik administration company</td><td>Name entry</td><td>Bavaria</td><td>54</td><td>12.02.19 AM</td></tr>
      <tr><td>Halvard International GmbH</td><td>Name entry</td><td>North Rhine-Westphalia</td><td>14</td><td>12.02.19 AM</td></tr>
      <tr><td>Brenntal Kompressoren GmbH</td><td>Name entry</td><td>Bavaria</td><td>45</td><td>12.02.19 AM</td></tr>
      <tr><td>Seefeld Logistik GmbH</td><td>Name entry</td><td>Hamburg</td><td>78</td><td>12.02.19 AM</td></tr>
      <tr><td>Halvard Europe GmbH</td><td>Name entry</td><td>Hesse</td><td>62</td><td>12.02.19 AM</td></tr>
      <tr><td>Ostwind Analytics GmbH</td><td>Name entry</td><td>North Rhine-Westphalia</td><td>78</td><td>12.02.19 AM</td></tr>
      <tr><td>Lindmark GmbH</td><td>Name entry</td><td>Bavaria</td><td>34</td><td>12.02.19 AM</td></tr>
      <tr><td>Garden of Agency</td><td>Name entry</td><td>Hesse</td><td>43</td><td>12.02.19 AM</td></tr>
    </tbody>
  </table>
</section>

<section class="cta">
  <div class="cta-photo" role="img" aria-label="Team of colleagues talking at a desk, tinted orange"></div>
  <h2 class="cta-title">HAVE QUESTION?<br>READY TO GET STARTED?</h2>
  <a class="btn" href="#">LETS' TALK!</a>
</section>

<footer class="site-footer">
  <svg class="footer-edge" viewBox="0 0 1200 62" preserveAspectRatio="none">
    <polygon points="0,62 1200,0 1200,62" fill="#151515"/>
    <polygon points="0,62 0,40 700,62" fill="#6a6a6a"/>
  </svg>
  <div class="footer-brand">
    <div class="brand"><span class="brand-square"></span>KONTORFELD</div>
    <p class="footer-tagline">WISSEN ÜBER REGISTERDATEN</p>
  </div>
  <div class="social" aria-label="Social links"><span></span><span></span><span></span><span></span></div>
  <div class="quick-links">
    <h3>QUICK LINKS</h3>
    <nav><a href="#">Home</a><a href="#">About us</a><a href="#">Our Services</a><a href="#">Support</a><a href="#">Contact</a></nav>
  </div>
  <p class="copyright">(c) 2020 Kontorfeld | All Rights Reserved | Disclaimer</p>
</footer>

</body>
</html>
```